Operating Model for KTR

Please convert the diagram on slide 3 to a professional design. Slides 1 and 2 gives a sense of the colour scheme - although not as bold as those - but sympathetic colours. But the KTR logo is to appear on the slide.
Further instructions in the slide

```html
<!DOCTYPE html>
<html lang="en">
<head>
<meta charset="utf-8">
<title>Operating Model for KTR</title>
<link href="https://fonts.googleapis.com/css2?family=Arimo:wght@400;700&display=swap" rel="stylesheet">
<style>
  :root {
    --bg: #cdd8dc;
    --magenta: #a8205e;
    --red: #d8202d;
    --salmon: #f08872;
    --ink: #262626;
    --white: #ffffff;
    --deco-dark: #8e1c22;
    --deco-light: #c4362e;
  }
  html, body {
    margin: 0;
    padding: 0;
    overflow: hidden;
    background: var(--bg);
  }
  .canvas {
    position: relative;
    width: 1200px;
    height: 676px;
    overflow: hidden;
    background: var(--bg);
    font-family: "Arimo", Arial, sans-serif;
  }
  .model {
    position: absolute;
    inset: 0;
    width: 1200px;
    height: 676px;
  }
  .segment { stroke: var(--bg); stroke-width: 5; }
  .seg-magenta { fill: var(--magenta); }
  .seg-red { fill: var(--red); }
  .seg-salmon { fill: var(--salmon); }
  .ring-seg { stroke: var(--bg); stroke-width: 3; }
  .pillar-title {
    font-family: "Arimo", Arial, sans-serif;
    font-weight: 700;
    font-size: 28px;
    letter-spacing: 1.5px;
    fill: var(--ink);
  }
  .sector-label {
    font-family: "Arimo", Arial, sans-serif;
    font-size: 12px;
    fill: var(--ink);
  }
  .ring-label {
    font-family: "Arimo", Arial, sans-serif;
    font-weight: 700;
    font-size: 11px;
    fill: var(--white);
  }
  .block {
    position: absolute;
    margin: 0;
    color: var(--white);
    font-size: 16px;
    line-height: 17px;
  }
  .block strong { font-weight: 700; }
  .block.all-bold { font-weight: 700; }
  .core-label {
    position: absolute;
    margin: 0;
    color: var(--white);
    font-weight: 700;
    font-size: 21px;
    line-height: 22px;
  }
  .decor-band {
    position: absolute;
    inset: 0;
  }
  .brand {
    position: absolute;
    left: 60px;
    top: 614px;
    display: flex;
    align-items: center;
    gap: 8px;
  }
  .brand-dot {
    width: 24px;
    height: 24px;
    border-radius: 50%;
    background: var(--magenta);
  }
  .brand-name {
    font-weight: 700;
    font-size: 18px;
    color: var(--ink);
    letter-spacing: 0.5px;
  }
</style>
</head>
<body>
<div class="canvas">

  <svg class="decor-band" viewBox="0 0 1200 676" role="img" aria-label="Decorative woven red and orange curved band pattern">
    <defs>
      <linearGradient id="bandFill" x1="0" y1="0" x2="1" y2="1">
        <stop offset="0" stop-color="var(--deco-light)"/>
        <stop offset="1" stop-color="var(--deco-dark)"/>
      </linearGradient>
    </defs>
    <path d="M1072 0 Q1182 338 1072 676 L1200 676 L1200 0 Z" fill="url(#bandFill)"/>
  </svg>

  <svg class="model" viewBox="0 0 1200 676" aria-hidden="true">
    <defs>
      <path id="headingArc" d="M135 496 A430 430 0 0 1 995 496"/>
      <path id="sectorArcOuter" d="M403 496 A162 162 0 0 1 727 496"/>
      <path id="sectorArcInner" d="M415 496 A150 150 0 0 1 715 496"/>
    </defs>

    <!-- Outer pillars -->
    <g class="pillars" transform="translate(565 496)">
      <g transform="rotate(0)"><path class="segment seg-magenta" d="M-405 0 A405 405 0 0 1 -364.89 -175.72 L-178.39 -85.91 A198 198 0 0 0 -198 0 Z"/></g>
      <g transform="rotate(25.714)"><path class="segment seg-magenta" d="M-405 0 A405 405 0 0 1 -364.89 -175.72 L-178.39 -85.91 A198 198 0 0 0 -198 0 Z"/></g>
      <g transform="rotate(51.429)"><path class="segment seg-magenta" d="M-405 0 A405 405 0 0 1 -364.89 -175.72 L-178.39 -85.91 A198 198 0 0 0 -198 0 Z"/></g>
      <g transform="rotate(77.143)"><path class="segment seg-magenta" d="M-405 0 A405 405 0 0 1 -364.89 -175.72 L-178.39 -85.91 A198 198 0 0 0 -198 0 Z"/></g>
      <g transform="rotate(102.857)"><path class="segment seg-red" d="M-405 0 A405 405 0 0 1 -364.89 -175.72 L-178.39 -85.91 A198 198 0 0 0 -198 0 Z"/></g>
      <g transform="rotate(128.571)"><path class="segment seg-red" d="M-405 0 A405 405 0 0 1 -364.89 -175.72 L-178.39 -85.91 A198 198 0 0 0 -198 0 Z"/></g>
      <g transform="rotate(154.286)"><path class="segment seg-salmon" d="M-405 0 A405 405 0 0 1 -364.89 -175.72 L-178.39 -85.91 A198 198 0 0 0 -198 0 Z"/></g>
    </g>

    <!-- Pillar headings -->
    <text class="pillar-title"><textPath href="#headingArc" startOffset="14%" text-anchor="middle">Planning for Skilling</textPath></text>
    <text class="pillar-title"><textPath href="#headingArc" startOffset="43%" text-anchor="middle">Attracting Students</textPath></text>
    <text class="pillar-title"><textPath href="#headingArc" startOffset="78%" text-anchor="middle">Building Future Skills</textPath></text>

    <!-- Education sectors -->
    <text class="sector-label"><textPath href="#sectorArcOuter" startOffset="11%" text-anchor="middle">Schooling</textPath></text>
    <text class="sector-label"><textPath href="#sectorArcOuter" startOffset="45%" text-anchor="middle">Community Education</textPath></text>
    <text class="sector-label"><textPath href="#sectorArcOuter" startOffset="75%" text-anchor="middle">Vocational</textPath></text>
    <text class="sector-label"><textPath href="#sectorArcInner" startOffset="75%" text-anchor="middle">Education</textPath></text>
    <text class="sector-label"><textPath href="#sectorArcOuter" startOffset="93%" text-anchor="middle">Higher</textPath></text>
    <text class="sector-label"><textPath href="#sectorArcInner" startOffset="93%" text-anchor="middle">Education</textPath></text>

    <!-- Stakeholder ring -->
    <g class="stakeholder-ring" transform="translate(566 492)">
      <g transform="rotate(0)"><path class="ring-seg seg-red" d="M-50.89 -132.57 A142 142 0 0 1 50.89 -132.57 L40.86 -106.43 A114 114 0 0 0 -40.86 -106.43 Z"/><text class="ring-label" x="0" y="-124" text-anchor="middle" dominant-baseline="middle">Government</text></g>
      <g transform="rotate(45)"><path class="ring-seg seg-magenta" d="M-50.89 -132.57 A142 142 0 0 1 50.89 -132.57 L40.86 -106.43 A114 114 0 0 0 -40.86 -106.43 Z"/><text class="ring-label" x="0" y="-124" text-anchor="middle" dominant-baseline="middle">Future Skills</text></g>
      <g transform="rotate(90)"><path class="ring-seg seg-magenta" d="M-50.89 -132.57 A142 142 0 0 1 50.89 -132.57 L40.86 -106.43 A114 114 0 0 0 -40.86 -106.43 Z"/></g>
      <g transform="rotate(-90)"><text class="ring-label" x="0" y="128" text-anchor="middle" dominant-baseline="middle">Productivity</text></g>
      <g transform="rotate(135)"><path class="ring-seg seg-magenta" d="M-50.89 -132.57 A142 142 0 0 1 50.89 -132.57 L40.86 -106.43 A114 114 0 0 0 -40.86 -106.43 Z"/></g>
      <g transform="rotate(-45)"><text class="ring-label" x="0" y="128" text-anchor="middle" dominant-baseline="middle">Quality</text></g>
      <g transform="rotate(180)"><path class="ring-seg seg-magenta" d="M-50.89 -132.57 A142 142 0 0 1 50.89 -132.57 L40.86 -106.43 A114 114 0 0 0 -40.86 -106.43 Z"/></g>
      <g transform="rotate(0)"><text class="ring-label" x="0" y="128" text-anchor="middle" dominant-baseline="middle">Feedback</text></g>
      <g transform="rotate(225)"><path class="ring-seg seg-red" d="M-50.89 -132.57 A142 142 0 0 1 50.89 -132.57 L40.86 -106.43 A114 114 0 0 0 -40.86 -106.43 Z"/></g>
      <g transform="rotate(45)"><text class="ring-label" x="0" y="128" text-anchor="middle" dominant-baseline="middle">Students</text></g>
      <g transform="rotate(270)"><path class="ring-seg seg-red" d="M-50.89 -132.57 A142 142 0 0 1 50.89 -132.57 L40.86 -106.43 A114 114 0 0 0 -40.86 -106.43 Z"/><text class="ring-label" x="0" y="-124" text-anchor="middle" dominant-baseline="middle">Industry</text></g>
      <g transform="rotate(315)"><path class="ring-seg seg-red" d="M-50.89 -132.57 A142 142 0 0 1 50.89 -132.57 L40.86 -106.43 A114 114 0 0 0 -40.86 -106.43 Z"/><text class="ring-label" x="0" y="-124" text-anchor="middle" dominant-baseline="middle">Community</text></g>

      <!-- Core -->
      <circle r="104" fill="var(--bg)"/>
      <circle r="101" class="seg-magenta"/>
      <path class="seg-red" d="M73 -70 C20 -20 20 0 0 0 C-20 0 -60 20 -72 74 A102 102 0 1 1 73 -70 Z"/>
    </g>
  </svg>

  <!-- Pillar content -->
  <p class="block all-bold" style="left:215px; top:404px;">Engagement<br>and<br>Collaboration<br>Front door</p>
  <p class="block all-bold" style="left:274px; top:292px;">Skills data<br>and insights</p>
  <p class="block" style="left:393px; top:180px;"><strong>Provision<br>Planning</strong><br>Regional<br>Skills Plan</p>
  <p class="block" style="left:532px; top:144px;"><strong>Student</strong><br>Acquisition<br>and<br>Guidance</p>
  <p class="block" style="left:664px; top:161px;"><strong>Skills</strong><br>Feedback<br>Employers<br>and<br>Students</p>
  <p class="block" style="left:772px; top:263px;"><strong>Quality</strong><br>workforce<br>course design<br>recognition</p>
  <p class="block" style="left:826px; top:424px;"><strong>Skills</strong><br>innovation</p>

  <p class="core-label" style="left:513px; top:421px;">Skills<br>Planning</p>
  <p class="core-label" style="left:545px; top:522px;">Skills<br>Renewal</p>

  <div class="brand">
    <span class="brand-dot"></span>
    <span class="brand-name">KTR</span>
  </div>
</div>
</body>
</html>
```